lantern reach collective non profit

I need a simple static website for a non-profit organization that includes blog capacity through Wordpress. The non-profit organization provides education and funding for alternative births and post natal care (doulas and mid-wives) for women. I have the domain name already but not the hosting. I've also set up a gmail account to link to the contact me page.
Updates

Also, would love warm colors.  Background can be white but toolbar and other accents could be peachy warm, tan / mauvish earthy colors.

Thanks.

Target Market(s)

The webstie will be for women who are going through the birthing process or have just given birth. Targeted toward women 16 to 50. The site will include various international outreach programs

Industry/Entity Type

Non Profit

Number of Pages Required

5+ pages

Requirements
Must have
• I want a site that I can control content after it has been designed. So I can add and change copy once it's up. It also must have photo and blog capacity (blog through Wordpress). Toolbar should include (with corresponding pages behind it that I will later include more info that I can update myself) Home, About, Resources / Links, Workshops, Members/Board, Donate Here-sponsors, Forum, International Outreach and somewhere on the homepage: Membership sign-up, Contact.
• The copy attached can be used on the home page.  Then where it explains about the founder, can be in the About section.

• Use warm tones - like peaches or mauvish earthy tan colors for the Toolbars.  (Background can be white.) 
• Use logo (attached) in banner on left and tagline: 
• Non-profit organization providing pre- and postnatal care for women.

• Would like the black and white photo with the mom's hands and baby's feet used as a constant photo and/or in the banner.
Nice to have
• Video capacity for me to add information.  This can be on the blog (through wordpress.)
Should not have
• No stiff, rigid lines.

```html
<!DOCTYPE html>
<html lang="en">
<head>
<meta charset="utf-8">
<title>Lantern Reach Collective</title>
<link rel="stylesheet" href="https://fonts.googleapis.com/css2?family=Pinyon+Script&family=Comic+Neue:wght@400;700&display=swap">
<style>
  :root {
    --page-pink: #fcdcfc;
    --button-pink: #f590b0;
    --button-shadow: rgba(60, 40, 50, 0.55);
    --band-light: #ffffff;
    --band-dark: #a89a86;
    --ink: #1a1a1a;
    --brand-blue: #23429a;
    --frame-pink: #fbc9dd;
    --photo-dark: #0c0c0c;
    --photo-mid: #6a6a6a;
  }
  * { margin: 0; padding: 0; box-sizing: border-box; }
  html, body { width: 1200px; height: 1200px; overflow: hidden; }
  body { position: relative; background: var(--page-pink); color: var(--ink); font-family: "Comic Neue", "Comic Sans MS", cursive; }

  .top-band, .bottom-band { position: absolute; left: 0; width: 1200px; }
  .top-band { top: 0; height: 102px; background: linear-gradient(to bottom, var(--band-dark) 0%, #d8d0c4 35%, var(--band-light) 100%); }
  .bottom-band { top: 1092px; height: 108px; background: linear-gradient(to bottom, var(--band-light) 0%, #e6e0d6 55%, var(--band-dark) 100%); }

  .quote { position: absolute; font-family: "Pinyon Script", cursive; font-size: 33px; color: var(--ink); white-space: nowrap; }
  .quote-line-one { left: 34px; top: 146px; }
  .quote-line-two { left: 22px; top: 220px; }

  .brand { position: absolute; left: 818px; top: 236px; display: flex; align-items: center; gap: 10px; }
  .brand-dot { width: 22px; height: 22px; border-radius: 50%; background: var(--brand-blue); }
  .brand-name { font-family: "Comic Neue", "Comic Sans MS", cursive; font-weight: 700; font-size: 22px; color: var(--brand-blue); white-space: nowrap; }

  .pill {
    position: absolute; background: var(--button-pink); color: var(--ink);
    box-shadow: 6px 6px 6px var(--button-shadow);
    display: flex; align-items: center; justify-content: center; text-align: center;
    font-size: 29px; line-height: 36px; text-decoration: none;
  }
  .main-nav .pill { top: 326px; height: 53px; width: 165px; }
  .nav-home { left: 82px; }
  .nav-about { left: 257px; }
  .nav-resources { left: 433px; }
  .nav-workshops { left: 607px; }
  .nav-members { left: 785px; }
  .nav-forum { left: 960px; }

  .action-links .pill { top: 962px; height: 80px; width: 200px; }
  .action-register { left: 96px; }
  .action-donate { left: 370px; }
  .action-outreach { left: 638px; }
  .action-contact { left: 908px; }

  .feature-photo {
    position: absolute; left: 52px; top: 438px; width: 372px; height: 428px;
    background: var(--frame-pink); padding: 14px;
    transform: rotate(-10deg); box-shadow: 6px 8px 10px rgba(60, 40, 50, 0.5);
  }
  .feature-photo-fill { width: 100%; height: 100%; background: radial-gradient(ellipse at 50% 45%, var(--photo-mid) 0%, #2a2a2a 45%, var(--photo-dark) 80%); }

  .welcome { position: absolute; left: 490px; top: 447px; font-size: 27px; line-height: 36px; white-space: nowrap; }
  .welcome-title { margin-bottom: 36px; }
</style>
</head>
<body>
  <header>
    <div class="top-band"></div>
    <p class="quote quote-line-one">“Help us help our sisters and daughters to take</p>
    <p class="quote quote-line-two">back control over how we bring the next generation to life.”</p>
    <div class="brand">
      <span class="brand-dot"></span>
      <span class="brand-name">Lantern Reach Collective</span>
    </div>
  </header>

  <nav class="main-nav">
    <a class="pill nav-home" href="#">Home</a>
    <a class="pill nav-about" href="#">About</a>
    <a class="pill nav-resources" href="#">Resources</a>
    <a class="pill nav-workshops" href="#">Workshops</a>
    <a class="pill nav-members" href="#">Members</a>
    <a class="pill nav-forum" href="#">Forum</a>
  </nav>

  <main>
    <figure class="feature-photo">
      <div class="feature-photo-fill" role="img" aria-label="Black and white photo of a mother's hands forming a heart around a baby's feet"></div>
    </figure>
    <section class="welcome">
      <h1 class="welcome-title" style="font-weight:400;font-size:27px;">Welcome</h1>
      <p>Lantern Reach Collective is a non-profit<br>
      organization dedicated to helping women find<br>
      better birthing methods and post-natal care by<br>
      providing FREE information and services<br>
      &nbsp;for mothers.&nbsp; In many cultures, having a baby<br>
      &nbsp;is part of a tribal community where women are<br>
      nurtured before, during and after birth.<br>
      Friends and family rally around and tend to<br>
      both mother and child.&nbsp; Birthing is a business<br>
      in America and it shouldn’t be.</p>
    </section>
  </main>

  <nav class="action-links">
    <a class="pill action-register" href="#">Register/<br>Sign In</a>
    <a class="pill action-donate" href="#">Donate Here/<br>Sponsor</a>
    <a class="pill action-outreach" href="#">International<br>Outreach</a>
    <a class="pill action-contact" href="#">Contact<br>Us</a>
  </nav>

  <footer>
    <div class="bottom-band"></div>
    <p class="quote" style="left:0;width:1200px;text-align:center;top:1112px;font-size:38px;">Non-profit organization providing pre- and postnatal care for women.</p>
  </footer>
</body>
</html>
```